Business Card Design

The name of my business is called Amber Lantern, Inc.

We are the first brick and mortar store in our state that will specialize in spy equipment. I don't want the term "spy equipment" used in the design of the card. I would like a double sided card with the one side having all my contact information and the other side having the company name and the quote "Discreet Surveillance Equipment". I'm not looking for the perfect card on the first try but am not looking to make many changes.

I would like the card to speak sophistication so I tend to lean toward dark color backgrounds.

Industry/Entity Type

Store

Contact Information for Business Card

Gerald Moravec, Consultant
483-917-6052
gerald.moravec@amberlantern.net
www.amberlantern.net

```html
<!DOCTYPE html>
<html lang="en">
<head>
<meta charset="utf-8">
<title>Amber Lantern, Inc. — Business Card</title>
<link href="https://fonts.googleapis.com/css2?family=Oswald:wght@400;500;600&display=swap" rel="stylesheet">
<style>
  :root {
    --stage: #1c1c1e;
    --card-top: #151517;
    --card-bottom: #060607;
    --red: #e3202a;
    --silver: #c9c9cb;
    --silver-soft: #a9a9ad;
  }
  * { box-sizing: border-box; margin: 0; padding: 0; }
  html, body {
    width: 1200px;
    height: 871px;
    overflow: hidden;
    background: var(--stage);
    font-family: "Oswald", "Arial Narrow", sans-serif;
  }
  .stage {
    width: 1200px;
    height: 871px;
    display: flex;
    flex-direction: column;
    align-items: center;
    justify-content: center;
    gap: 40px;
  }
  .card {
    position: relative;
    width: 680px;
    height: 389px;
    background: linear-gradient(160deg, var(--card-top), var(--card-bottom));
    box-shadow: 0 10px 30px rgba(0,0,0,0.5);
  }

  /* Back side: company name and tagline */
  .card-back {
    display: flex;
    flex-direction: column;
    align-items: center;
    justify-content: center;
    gap: 6px;
  }
  .wordmark {
    display: flex;
    align-items: center;
    gap: 14px;
    color: var(--silver);
    font-weight: 500;
    letter-spacing: 2px;
    text-transform: uppercase;
  }
  .wordmark-square {
    width: 18px;
    height: 18px;
    background: var(--red);
  }
  .card-back .wordmark { font-size: 40px; }
  .card-back .wordmark-square { width: 24px; height: 24px; }
  .tagline {
    color: var(--red);
    font-size: 22px;
    font-weight: 500;
    letter-spacing: 3px;
    text-transform: uppercase;
  }

  /* Front side: contact details */
  .card-front .brand {
    position: absolute;
    left: 0;
    width: 330px;
    top: 0;
    bottom: 0;
    display: flex;
    align-items: center;
    justify-content: center;
  }
  .card-front .wordmark { font-size: 25px; }
  .divider {
    position: absolute;
    left: 330px;
    top: 88px;
    width: 2px;
    height: 214px;
    background: var(--red);
  }
  .contact {
    position: absolute;
    left: 360px;
    top: 104px;
  }
  .contact-name {
    color: var(--silver);
    font-size: 34px;
    font-weight: 600;
    letter-spacing: 2px;
    text-transform: uppercase;
    line-height: 1.1;
  }
  .contact-role {
    color: var(--red);
    font-size: 20px;
    font-weight: 500;
    letter-spacing: 1px;
    margin-bottom: 12px;
  }
  .contact-list { list-style: none; }
  .contact-list li {
    display: flex;
    align-items: center;
    gap: 12px;
    color: var(--silver-soft);
    font-size: 17px;
    letter-spacing: 0.5px;
    line-height: 30px;
  }
  .contact-icon {
    width: 14px;
    height: 14px;
    flex: none;
    fill: var(--red);
  }
</style>
</head>
<body>
<main class="stage">
  <section class="card card-back" aria-label="Card back">
    <div class="wordmark"><span class="wordmark-square"></span>Amber Lantern, Inc</div>
    <p class="tagline">Discreet Surveillance Equipment</p>
  </section>

  <section class="card card-front" aria-label="Card front">
    <div class="brand">
      <div class="wordmark"><span class="wordmark-square"></span>Amber Lantern, Inc</div>
    </div>
    <div class="divider"></div>
    <div class="contact">
      <h1 class="contact-name">Gerald Moravec</h1>
      <p class="contact-role">Consultant</p>
      <ul class="contact-list">
        <li>
          <svg class="contact-icon" viewBox="0 0 16 16" aria-hidden="true"><path d="M1 5c0-2 2-3 7-3s7 1 7 3v1.5h-3.5V5h-7v1.5H1z M3 8h10l1.5 6h-13z M6 9.5a2 2 0 1 0 4 0 2 2 0 1 0-4 0z" /></svg>
          483-917-6052
        </li>
        <li>
          <svg class="contact-icon" viewBox="0 0 16 16" aria-hidden="true"><path d="M1 3h14v1.2L8 9 1 4.2z M1 5.8 8 10.6l7-4.8V13H1z"/></svg>
          gerald.moravec@amberlantern.net
        </li>
        <li>
          <svg class="contact-icon" viewBox="0 0 16 16" aria-hidden="true"><path fill-rule="evenodd" d="M8 1a7 7 0 1 1 0 14A7 7 0 0 1 8 1zm0 1.3c-.9 1-1.5 2.8-1.6 4.9h3.2C9.5 5.1 8.9 3.3 8 2.3zM2.4 7.2h2.7c.1-1.9.5-3.5 1.2-4.6A5.7 5.7 0 0 0 2.4 7.2zm8.5 0h2.7a5.7 5.7 0 0 0-3.9-4.6c.7 1.1 1.1 2.7 1.2 4.6zM2.4 8.8a5.7 5.7 0 0 0 3.9 4.6c-.7-1.1-1.1-2.7-1.2-4.6zm4 0c.1 2.1.7 3.9 1.6 4.9.9-1 1.5-2.8 1.6-4.9zm4.5 0c-.1 1.9-.5 3.5-1.2 4.6a5.7 5.7 0 0 0 3.9-4.6z"/></svg>
          www.amberlantern.net
        </li>
      </ul>
    </div>
  </section>
</main>
</body>
</html>
```